Online-Marketing Material für Bewegungsangebot speziell für Kinder
Zielgruppe
Hopsalino bietet ein hochwertiges, sportwissenschaftlich fundiertes Bewegungsangebot speziell für Kinder an. Unsere Kurse verbinden spielerische Elemente mit modernen Trainingsmethoden und schaffen eine liebevolle Umgebung in der Kinder ganz ohne Druck wachsen, lernen und sich mit Freude bewegen.
Unsere Zielgruppe sind Eltern mit Kindern zwischen zwei und acht Jahren, die ein qualitativ sehr hochwertiges Sportprogramm für ihre Kinder suchen und großen Wert auf professionelle Förderung, Sicherheit und eine warmherzige Atmosphäre legen.
Aufgabenstellung
Die Kreativen sollen berücksichtigen, dass der neue Hero ein echter Eye Catcher sein muss. Er soll sofort ein Wow-Gefühl auslösen und viel stärker auffallen als die aktuelle, eher schlichte Hero Section. Die Gestaltung soll hochwertig, kindlich liebevoll und gleichzeitig modern wirken. Der neue Hero muss sich perfekt in das bestehende Webdesign einfügen und die Hopsalino Welt auf den ersten Blick spürbar machen. Der bestehende Text bleibt zwingend erhalten. Alles andere darf kreativ neu gedacht werden, solange das Ergebnis direkt Aufmerksamkeit fängt, Emotionen weckt und die hohe Qualität des Sportangebots im Kindersegment sichtbar macht.
Ich benötige ein vollständiges Redesign ausschließlich für die Hero Section meiner Website www.hopsalino-kurse.example. Das restliche Webdesign passt bereits sehr gut zu meiner Marke, doch die aktuelle Hero Section wirkt noch zu schlicht und erzeugt kein echtes Wow-Gefühl.
Hopsalino steht für ein hochwertiges, sportwissenschaftlich fundiertes Sportangebot für Kinder zwischen zwei und acht Jahren. Unsere Welt ist liebevoll, warm, spielerisch und gleichzeitig sehr professionell. Genau dieses Gefühl soll der neue Hero sofort transportieren.
Wichtige Vorgaben
• Es geht ausschließlich um die Hero Section
• Der bestehende Text muss unbedingt erhalten bleiben
• Das Design soll hochwertig, kindlich, warm und liebevoll wirken
• Optisch nahtlose Anpassung an das bestehende Webdesign
• Der neue Hero soll ein klarer Eye Catcher sein und ein echtes Wow erzeugen
• Kreative Freiheit in der Gestaltung, solange alles modern, hochwertig und zur Hopsalino Welt passend bleibt
Mir ist wichtig, dass der neue Hero direkt Emotionen weckt und die hohe Qualität unseres Kinder-Sportangebots schon auf den ersten Blick spürbar macht.

```html
<!DOCTYPE html>
<html lang="de">
<head>
<meta charset="utf-8">
<title>Hopsalino – Hero</title>
<link rel="stylesheet" href="https://fonts.googleapis.com/css2?family=Outfit:wght@500;600;800&family=Poppins:wght@400;500;600&display=swap">
<style>
  :root {
    --ink: #1d1a16;
    --gold: #c69a2e;
    --gold-light: #e2c168;
    --cream: #fbf5e6;
    --cream-soft: #fffdf7;
    --muted: #3a342c;
  }
  * { margin: 0; padding: 0; box-sizing: border-box; }
  html, body { width: 1200px; height: 704px; overflow: hidden; }
  body {
    background: radial-gradient(ellipse at 20% 30%, var(--cream) 0%, var(--cream-soft) 60%, #fffefb 100%);
    font-family: "Poppins", sans-serif;
    color: var(--ink);
    position: relative;
  }
  .hero { position: absolute; inset: 0; overflow: hidden; }

  .site-header {
    position: absolute; top: 34px; left: 104px; right: 104px;
    display: flex; align-items: center;
  }
  .brand {
    display: flex; align-items: center; gap: 10px;
    font-family: "Outfit", sans-serif; font-weight: 800; font-size: 20px; color: var(--ink);
  }
  .brand-dot {
    width: 22px; height: 22px; border-radius: 50%;
    border: 3px solid var(--gold);
  }
  .main-nav {
    position: absolute; left: 211px; display: flex; gap: 28px;
    font-size: 14px; font-weight: 500;
  }
  .main-nav .sep { color: var(--muted); }

  .intro { position: absolute; left: 104px; top: 190px; width: 540px; }
  .welcome-pill {
    display: inline-flex; align-items: center; gap: 7px;
    border: 1.5px solid var(--ink); border-radius: 20px;
    padding: 3px 16px 3px 8px; font-size: 13px; font-weight: 500;
  }
  .welcome-pill svg { width: 13px; height: 13px; }
  .headline {
    margin-top: 14px;
    font-family: "Outfit", sans-serif; font-weight: 800;
    font-size: 57px; line-height: 1.0; letter-spacing: -0.5px;
    text-transform: uppercase;
  }
  .headline .accent {
    background: linear-gradient(180deg, var(--gold-light), var(--gold));
    -webkit-background-clip: text; background-clip: text; color: transparent;
  }
  .lead {
    margin-top: 26px; width: 500px;
    font-size: 11.5px; line-height: 1.55; color: var(--muted);
  }
  .cta {
    display: inline-block; margin-top: 26px;
    padding: 10px 30px; border-radius: 20px;
    background: linear-gradient(180deg, var(--gold-light), var(--gold));
    color: #fff; font-family: "Outfit", sans-serif; font-weight: 600; font-size: 14px;
    text-transform: uppercase; text-decoration: none;
  }

  .ring { position: absolute; left: 0; top: 0; }
  .ball { position: absolute; border-radius: 50%; }
  .ball-basket { left: 540px; top: 554px; width: 150px; height: 150px;
    background: radial-gradient(circle at 40% 35%, #e8c66e, #b8891f); }
  .ball-volley { left: 1110px; top: 530px; width: 160px; height: 160px;
    background: radial-gradient(circle at 40% 35%, #ffffff, #e7e1d3); }
  .ball-soccer-faint { left: -60px; top: 560px; width: 150px; height: 150px;
    background: radial-gradient(circle, rgba(230,225,215,0.55), rgba(230,225,215,0.15)); }
  .mascot {
    position: absolute; left: 690px; top: 100px; width: 440px; height: 604px;
    border-radius: 48% 48% 8px 8px;
    background: linear-gradient(180deg, #d98a32 0%, #d98a32 42%, #2aa0d8 52%, #2aa0d8 72%, #3b3833 84%, #5a4a3a 100%);
    opacity: 0.9;
  }
</style>
</head>
<body>
<main class="hero">
  <svg class="ring" width="1200" height="704" viewBox="0 0 1200 704" aria-hidden="true">
    <circle cx="914" cy="858" r="460" fill="none" stroke="#d3a63a" stroke-width="14"/>
  </svg>
  <div class="ball ball-soccer-faint" role="img" aria-label="Blasser Fußball als Dekoration"></div>
  <div class="ball ball-basket" role="img" aria-label="Goldener Basketball"></div>
  <div class="ball ball-volley" role="img" aria-label="Weißer Volleyball"></div>
  <div class="mascot" role="img" aria-label="Maskottchen-Bär im blauen Trikot mit Daumen hoch"></div>

  <header class="site-header">
    <div class="brand"><span class="brand-dot"></span>Hopsalino</div>
    <nav class="main-nav">
      <span>Konzept</span><span class="sep">/</span><span>Franchise</span><span class="sep">/</span><span>Kontakt</span>
    </nav>
  </header>

  <section class="intro">
    <span class="welcome-pill">
      <svg viewBox="0 0 14 14"><circle cx="7" cy="7" r="6" fill="none" stroke="#1d1a16" stroke-width="1.5"/><circle cx="7" cy="7" r="2.2" fill="#1d1a16"/></svg>
      Willkommen Bei Hopsalino
    </span>
    <h1 class="headline">Deine <span class="accent">Ballschule</span><br><span class="accent">für</span> Kinder ab 2<br>Jahren</h1>
    <p class="lead">Stinkbomben ausweichen, Balli retten und ins Weltall fliegen. Bei Hopsalino werden Kinder nicht nur zu kleinen Bewegungsprofis, bei uns geht es um weit mehr. Motorik, Koordination und gezieltes Gehirntraining fördern die Entwicklung deines Kindes spielerisch und ganzheitlich in einer liebevollen Umgebung.</p>
    <a class="cta" href="#">Kurs in deiner Nähe finden</a>
  </section>
</main>
</body>
</html>
```